Mortgage Broking Business Card Design

We are a mortgage broking business. We offer mortgage solutions and make them easy.

The business motto will be "Home lending, clearly explained"

Our business will essentially act as an interpreter to Banking/mortgages. We offer home loans, business loans and leases

The colours of the business card should be bright but professional e.g. orange and black (maybe)??
Updates

Please note the QLNB logo that needs to be on the business card does NOT need to be in the blue and green colours. It can be in the same colours as the rest of the business card. Thanks

Target Market(s)

Mums and Dads, small business, first home buyers, anyone that needs a home loan or a loan

Industry/Entity Type

Business

Contact Information for Business Card

Carla Dunwick
Credit Adviser

VELTA MORTGAGES
"Home lending, clearly explained"

1300 472 639
0413 786 512

carla@veltamortgages-example.com.au
www.veltamortgages-example.com.au

Credit Representative Number 738254

Requirements
Must have
• the QLNB logo that I have downloaded in the images above should be somewhere on the business card, so that customers can see that I am QLNB certified. This can be in Black to suit the colours of the business card

My Credit Representative Number 738254 needs to also be displayed somewhere

```html
<!DOCTYPE html>
<html lang="en">
<head>
<meta charset="utf-8">
<title>Velta Mortgages – Business Card</title>
<link rel="stylesheet" href="https://fonts.googleapis.com/css2?family=Ubuntu:wght@400;500;700&display=swap">
<style>
  :root {
    --backdrop: #d9d9d7;
    --card-white: #f2f1ee;
    --card-black: #1e1e1e;
    --brand-orange: #e0901f;
    --icon-yellow: #f2c417;
    --ink-dark: #2a2a2a;
    --ink-grey: #555555;
    --ink-light: #f4f4f4;
  }
  * { box-sizing: border-box; margin: 0; padding: 0; }
  html, body {
    width: 1200px; height: 1000px; overflow: hidden;
    background: var(--backdrop);
    font-family: "Ubuntu", sans-serif;
  }
  .business-card {
    position: absolute; left: 150px; top: 225px;
    width: 900px; height: 550px;
    display: flex;
    box-shadow: 0 10px 30px rgba(0,0,0,0.18);
  }
  .card-front-brand {
    position: relative;
    width: 370px; background: var(--card-white);
  }
  .brand-lockup {
    position: absolute; left: 0; right: 0; top: 170px;
    text-align: center;
  }
  .brand-name {
    display: inline-flex; align-items: center; gap: 10px;
    font-weight: 700; font-size: 30px; color: var(--ink-dark);
    letter-spacing: 0.5px; white-space: nowrap;
  }
  .brand-mark {
    width: 22px; height: 22px; background: var(--brand-orange);
  }
  .brand-tagline {
    margin-top: 6px; font-size: 18px; color: var(--ink-grey);
    white-space: nowrap;
  }
  .accent-bar {
    position: absolute; left: 0; top: 430px;
    width: 330px; height: 12px; background: var(--brand-orange);
  }
  .card-contact-panel {
    position: relative; flex: 1;
    background: var(--card-black); color: var(--ink-light);
    padding: 70px 0 0 40px;
  }
  .adviser-name { font-size: 32px; font-weight: 500; }
  .adviser-title { font-size: 18px; margin-top: 2px; }
  .contact-icons { display: flex; gap: 14px; margin-top: 24px; }
  .contact-icon {
    width: 36px; height: 36px; border-radius: 50%;
    background: var(--icon-yellow);
    display: flex; align-items: center; justify-content: center;
  }
  .contact-lines { margin-top: 26px; font-size: 22px; line-height: 1.32; }
  .credit-rep { margin-top: 18px; font-size: 22px; }
  .certification-badge {
    position: absolute; right: 60px; bottom: 50px;
    width: 150px; height: 50px;
    border: 2px solid var(--ink-light);
  }
</style>
</head>
<body>
  <div class="business-card">
    <section class="card-front-brand">
      <div class="brand-lockup">
        <div class="brand-name"><span class="brand-mark"></span>VELTA MORTGAGES</div>
        <div class="brand-tagline">Home lending, clearly explained</div>
      </div>
      <div class="accent-bar"></div>
    </section>
    <section class="card-contact-panel">
      <h1 class="adviser-name">Carla Dunwick</h1>
      <p class="adviser-title">Credit Adviser</p>
      <div class="contact-icons">
        <span class="contact-icon">
          <svg width="18" height="18" viewBox="0 0 24 24"><path fill="#1e1e1e" d="M6.6 10.8a15.1 15.1 0 0 0 6.6 6.6l2.2-2.2a1 1 0 0 1 1-.25 11.4 11.4 0 0 0 3.6.57 1 1 0 0 1 1 1V20a1 1 0 0 1-1 1A17 17 0 0 1 3 4a1 1 0 0 1 1-1h3.5a1 1 0 0 1 1 1c0 1.25.2 2.45.57 3.57a1 1 0 0 1-.25 1z"/></svg>
        </span>
        <span class="contact-icon">
          <svg width="18" height="18" viewBox="0 0 24 24"><rect x="3" y="6" width="18" height="12" fill="none" stroke="#1e1e1e" stroke-width="2"/><path d="M3 6l9 7 9-7" fill="none" stroke="#1e1e1e" stroke-width="2"/></svg>
        </span>
        <span class="contact-icon">
          <svg width="18" height="18" viewBox="0 0 24 24" fill="none" stroke="#1e1e1e" stroke-width="2"><circle cx="12" cy="12" r="9"/><path d="M3 12h18M12 3c3 3 3 15 0 18M12 3c-3 3-3 15 0 18"/></svg>
        </span>
      </div>
      <div class="contact-lines">
        <p>1300 472 639, 0413 786 512</p>
        <p>carla@veltamortgages-example.com.au</p>
        <p>www.veltamortgages-example.com.au</p>
      </div>
      <p class="credit-rep">Credit Representative Number 738254</p>
      <div class="certification-badge" role="img" aria-label="Accreditation badge"></div>
    </section>
  </div>
</body>
</html>
```